RedField - Rebranding, Namecard, Stationary and One Page Web

Refresh logo, make it modern and design matching name card, stationary and one page web

RedField Information Technology (Int'l) Company Limited
紅原訊息科技(國際)有限公司

Company is System Integrator, and will be providing products and services to government and enterprise organizations. Our Chief Security Officer came from top U.S. vendor, and had been working on top enterprise and government projects globally, so we want the refreshed image of the new company to have a East Cost U.S. style, with hint of technology from Silicon Valley. The company will also be representing top brands from the U.S. on information security.

Branding refresh is needed because company is being acquired and is expanding

Target Market(s)

Cyber Security

Industry/Entity Type

Information Technology

Contact Information for Business Card

Need Chinese and English

Number of Pages Required

1 page

Font styles to use
Sans Serif

Colors
0292cd
00a990

Requirements
Must have
• Modern, clean, cyber look. Must keep same colors and general look and feel of original logo. Only modernization, do not change its personality

```html
<!DOCTYPE html>
<html lang="en">
<head>
<meta charset="utf-8">
<title>RedField Name Cards</title>
<link href="https://fonts.googleapis.com/css2?family=Noto+Sans:wght@400;600&family=Noto+Sans+TC:wght@400;500&family=Orbitron:wght@500&family=Exo+2:ital,wght@1,800&display=swap" rel="stylesheet">
<style>
  :root {
    --canvas: #dcdde0;
    --card-light: #ffffff;
    --card-dark: #231f20;
    --brand-blue: #5a9cc5;
    --brand-green: #6dbb5c;
    --ink: #2b2b2b;
    --ink-light: #ffffff;
  }
  * { margin: 0; padding: 0; box-sizing: border-box; }
  html, body { width: 1200px; height: 780px; overflow: hidden; background: var(--canvas); }
  body { position: relative; font-family: "Noto Sans", "Noto Sans TC", sans-serif; color: var(--ink); }

  .card {
    position: absolute; width: 490px; height: 298px; border-radius: 19px;
    box-shadow: 0 2px 6px rgba(0,0,0,.12);
  }
  .card--front { background: var(--card-light); top: 74px; }
  .card--back { background: var(--card-dark); top: 408px; }
  .card--a { left: 74px; }
  .card--b { left: 636px; }

  .front-mark {
    position: absolute; left: 22px; top: 130px; width: 140px; text-align: center;
    font-family: "Noto Sans", sans-serif; font-weight: 600; font-size: 25px;
    color: var(--brand-blue);
  }

  .details { position: absolute; left: 188px; top: 60px; }
  .details__name { font-family: "Orbitron", sans-serif; font-weight: 500; font-size: 18px; letter-spacing: .5px; color: var(--brand-blue); line-height: 1.2; }
  .card--b .details__name { font-family: "Exo 2", sans-serif; font-style: italic; font-weight: 800; font-size: 19px; letter-spacing: 1px; }
  .details__title { font-size: 13.5px; color: var(--brand-green); line-height: 1.3; margin-bottom: 7px; }
  .contact { list-style: none; margin-bottom: 6px; }
  .contact li { display: flex; align-items: center; font-size: 14px; line-height: 18.5px; }
  .contact svg { width: 12px; height: 12px; margin-right: 5px; fill: var(--brand-green); flex: none; }
  .address { font-style: normal; font-size: 14px; line-height: 17px; }
  .address__zh { font-family: "Noto Sans TC", sans-serif; font-size: 11.5px; margin-top: 3px; }

  .back-mark {
    position: absolute; left: 0; right: 0; top: 100px; text-align: center;
    font-family: "Noto Sans", sans-serif; font-weight: 600; font-size: 60px;
    color: var(--brand-blue); line-height: 1;
  }
  .company { position: absolute; left: 0; right: 0; top: 240px; text-align: center; color: var(--ink-light); }
  .company__en { font-size: 15px; line-height: 20px; }
  .company__zh { font-family: "Noto Sans TC", sans-serif; font-size: 12px; line-height: 20px; }
</style>
</head>
<body>

<svg width="0" height="0" style="position:absolute">
  <symbol id="icon-phone" viewBox="0 0 12 12"><path d="M3 0h6a1 1 0 0 1 1 1v10a1 1 0 0 1-1 1H3a1 1 0 0 1-1-1V1a1 1 0 0 1 1-1zm.6 1.5v8h4.8v-8z"/></symbol>
  <symbol id="icon-mail" viewBox="0 0 12 12"><path d="M0 2h12v1.2L6 7 0 3.2zM0 4.6l6 3.8 6-3.8V10H0z"/></symbol>
  <symbol id="icon-globe" viewBox="0 0 12 12"><circle cx="6" cy="6" r="5.5"/><path d="M.5 6h11M6 .5v11M2 3h8M2 9h8" stroke="#fff" stroke-width=".7" fill="none"/></symbol>
</svg>

<section class="card card--front card--a">
  <div class="front-mark">RedField</div>
  <div class="details">
    <div class="details__name">DANIEL WONG</div>
    <div class="details__title">CEO</div>
    <ul class="contact">
      <li><svg><use href="#icon-phone"/></svg>(852) 5120 4417</li>
      <li><svg><use href="#icon-mail"/></svg>danielwong@HKRedField.com.hk</li>
      <li><svg><use href="#icon-globe"/></svg>www.HKRedField.com.hk</li>
    </ul>
    <address class="address">
      Room B, Unit 402, 4/F, Lok Tin Ind. Bldg.<br>
      No. 15 Sheung Yee Road<br>
      Kowloon Bay, Kowloon, HKSAR
      <div class="address__zh">香港九龍灣常怡道15樂天工業大廈4樓402 – B室</div>
    </address>
  </div>
</section>

<section class="card card--front card--b">
  <div class="front-mark">RedField</div>
  <div class="details">
    <div class="details__name">DANIEL WONG</div>
    <div class="details__title">CEO</div>
    <ul class="contact">
      <li><svg><use href="#icon-phone"/></svg>(852) 5120 4417</li>
      <li><svg><use href="#icon-mail"/></svg>danielwong@HKRedField.com.hk</li>
      <li><svg><use href="#icon-globe"/></svg>www.HKRedField.com.hk</li>
    </ul>
    <address class="address">
      Room B, Unit 402, 4/F, Lok Tin Ind. Bldg.<br>
      No. 15 Sheung Yee Road<br>
      Kowloon Bay, Kowloon, HKSAR
      <div class="address__zh">香港九龍灣常怡道15樂天工業大廈4樓402 – B室</div>
    </address>
  </div>
</section>

<section class="card card--back card--a">
  <div class="back-mark">RedField</div>
  <div class="company">
    <div class="company__en">RedField Information Technology (Int'l) Company Limited</div>
    <div class="company__zh">紅原訊息科技(國際)有限公司</div>
  </div>
</section>

<section class="card card--back card--b">
  <div class="back-mark">RedField</div>
  <div class="company">
    <div class="company__en">RedField Information Technology (Int'l) Company Limited</div>
    <div class="company__zh">紅原訊息科技(國際)有限公司</div>
  </div>
</section>

</body>
</html>
```